Gym Menu

Hi,

I would like to create a menu for my fitness center/ Dance school.

I do have a picture of how i would like it to look like ill attach it down there and instead of the Mexican looking icons i would like to have gym related icons example (Bar bell, dumbbells, etc..)

The menu will consist of the following

Smoothies
- Lagoon Waltz (20 SR)
(Kiwi, Pineapple, Banana, Grapes)
-Coral Drift (20 SR)
(Orange, Peach, Pineapple)
-Tidy Kick (20 SR)
(Carrot, Mango, Orange)
-Purple Thunder (20 SR)
(Blackberry, Raspberry, Banana)
-Cool Breeze (20 SR)
( Lemonade, Mint)
-Ruby Lantern (20 SR)
(Lemonade, Strawberry, Mint)

Mean Green Juices

-Quick Sprout (20SR)
(Cucumber, Celery, Green Apple, Spinach, Lemon, Ginger)
-Hop To It Now! (20 SR)
(Carrots, Apple, Beetroot)

Shake It Up

-Dusky Swirl (20 SR)
(Mocha, Skimmed Milk)

- Velvet Tumbler
(Chocolate, Skimmed Milk)

-Big Lift Zest

(Peanut Butter, Honey, Skimmed Milk, Banana) (20 SR)

Yummy Bites

- Zataar Croissant (10 SR)
- Cheese Croissant (10 SR)
- Plane Croissant (10 SR)
- Blueberry Muffin (7 SR)
- Chocolate Muffin (7 SR)
- Vanilla Muffin (7SR)
- Cookies (7 SR)
- Brownie (10 SR)
-Fresh Berry Popsicle (10 SR)
- Fresh Orange Popsicle (10 SR)

Make it Lite

-Garden Salad (15 SR)
-Greek Salad (15 SR)
-Ceaser Salad (15 SR)
-Italian Salad (15 SR)
- Tuna Sandwich (25 SR)
- Turkey Sandwich (25 SR)
- Chicken Sandwich (25 SR)
-Happy Patch Bowls (8SR)
- Mixed Nuts (10 SR)

Coffee and tea
- Americano (10 SR)
- Espresso (10 SR)
- Turkish Coffee (10 SR)
- Cappuccino (15 SR)
- Cafe Latte (15 SR)
-Hot Cacao (15 SR)
-Extra shor + 5SR

- Green Tea (10 SR)
- Earl Grey (10 SR)
- English Breakfast (10SR)

• The gyms color is orange ... i want this to be in the menu

the gyms name is vartomel i also want this in big somewhere

Colors of the menu should be

Orange
Yellow
green
red

all shades

```html
<!DOCTYPE html>
<html lang="en">
<head>
<meta charset="utf-8">
<title>Vartomel Menu</title>
<link rel="stylesheet" href="https://fonts.googleapis.com/css2?family=Oswald:wght@700&family=Questrial&display=swap">
<style>
  :root{
    --paper-light:#f7c24a;
    --paper-mid:#eea233;
    --paper-deep:#d9741f;
    --red:#b3141b;
    --ink:#ffffff;
    --divider:#3a1c0c;
  }
  *{margin:0;padding:0;box-sizing:border-box}
  html,body{width:1200px;height:849px;overflow:hidden;background:var(--paper-mid)}
  .menu{
    position:relative;width:1200px;height:849px;overflow:hidden;
    font-family:"Questrial",sans-serif;color:var(--ink);
    background:radial-gradient(ellipse at 50% 45%,var(--paper-light) 0%,var(--paper-mid) 55%,var(--paper-deep) 100%);
  }
  .page-divider{position:absolute;left:599px;top:0;width:2px;height:849px;background:var(--divider)}
  .tile{position:absolute}
  .panel{position:absolute}
  .panel h2{font-size:12px;font-weight:400;letter-spacing:1px;text-transform:uppercase;font-family:"Questrial",sans-serif}
  .item{display:flex;justify-content:space-between;font-size:13px;letter-spacing:1.3px;text-transform:uppercase;line-height:17px;white-space:nowrap}
  .desc{font-size:9.5px;letter-spacing:.6px;text-transform:uppercase;line-height:12px;opacity:.95}
  .wordmark{position:absolute;font-family:"Oswald",sans-serif;font-weight:700;color:var(--red);line-height:1;text-transform:uppercase;white-space:nowrap}
  .wordmark-left{left:166px;top:744px;font-size:49px;letter-spacing:1px}
  .wordmark-top{right:12px;top:28px;font-size:39px;letter-spacing:.5px}
  .wordmark-bottom{left:743px;top:786px;font-size:30px;letter-spacing:0}

  .smoothies{left:0;top:61px;width:339px;height:245px;background:linear-gradient(90deg,#dd3f1b,#ec7422)}
  .smoothies h2{position:absolute;top:15px;left:0;width:230px;text-align:center;font-weight:700}
  .smoothies .list{position:absolute;left:35px;top:45px;width:285px;display:flex;flex-direction:column;gap:2px}

  .greens{left:236px;top:309px;width:364px;height:194px;background:linear-gradient(90deg,#2d8a3a,#4f9e36)}
  .greens h2{position:absolute;left:14px;top:29px;font-weight:700}
  .greens .list{position:absolute;left:14px;top:58px;width:333px;display:flex;flex-direction:column;gap:16px}

  .shakes{left:0;top:511px;width:400px;height:221px;background:linear-gradient(90deg,#f08a1c,#f5a231)}
  .shakes .inner{position:absolute;left:25px;top:22px;width:355px}
  .shakes h2{font-size:13px;letter-spacing:1.5px;margin:0 0 12px}
  .shakes .group{margin-bottom:12px}

  .bites{left:635px;top:0;width:365px;height:274px;background:linear-gradient(180deg,#2b8539,#3d9638)}
  .bites h2{position:absolute;top:21px;left:0;width:100%;text-align:center;font-weight:700}
  .bites .list{position:absolute;left:31px;top:53px;width:315px}

  .lite{left:780px;top:287px;width:420px;height:216px;background:linear-gradient(90deg,#8f2512,#bd4319)}
  .lite h2{position:absolute;top:11px;left:0;width:420px;text-align:center;font-size:13px;letter-spacing:1.5px}
  .lite .list{position:absolute;left:33px;top:44px;width:370px}

  .coffee{left:600px;top:536px;width:342px;height:245px;background:linear-gradient(90deg,#ee861f,#f39a2a)}
  .coffee h2{position:absolute;left:31px;top:17px;font-size:13px;letter-spacing:1.5px}
  .coffee .list{position:absolute;left:31px;top:45px;width:297px}
  .coffee .item{font-size:12.5px;line-height:15.5px}
  .coffee .spacer{height:15px}
</style>
</head>
<body>
<main class="menu">
  <div class="page-divider"></div>

  <div class="tile" style="left:354px;top:0;width:113px;height:151px;background:#5fae46" role="img" aria-label="Pineapple icon"></div>
  <div class="tile" style="left:472px;top:86px;width:112px;height:126px;background:#e0441e" role="img" aria-label="Grape bunch icon"></div>
  <div class="tile" style="left:348px;top:172px;width:116px;height:104px;background:#efb236" role="img" aria-label="Push-up handles icon"></div>
  <div class="tile" style="left:0;top:320px;width:135px;height:157px;background:#f0a12c" role="img" aria-label="Strawberries icon"></div>
  <div class="tile" style="left:150px;top:318px;width:75px;height:73px;background:#4f9f3d" role="img" aria-label="Lime slice icon"></div>
  <div class="tile" style="left:150px;top:398px;width:75px;height:80px;background:#f1bb35" role="img" aria-label="Orange fruit icon"></div>
  <div class="tile" style="left:466px;top:538px;width:126px;height:133px;background:#dc3a1c" role="img" aria-label="Banana bunch icon"></div>
  <div class="tile" style="left:403px;top:677px;width:133px;height:130px;background:#ef8e26" role="img" aria-label="Halved orange icon"></div>
  <div class="tile" style="left:0;top:718px;width:155px;height:88px;background:#9fae3a" role="img" aria-label="Barbell icon"></div>

  <section class="panel smoothies">
    <h2>Smoothies</h2>
    <div class="list">
      <div><div class="item"><span>Lagoon Waltz</span><span>(20 SR)</span></div><div class="desc">(Kiwi, Pineapple, Banana, Grapes)</div></div>
      <div><div class="item"><span>Coral Drift</span><span>(20 SR)</span></div><div class="desc">(Orange, Peach, Pineapple)</div></div>
      <div><div class="item"><span>Tidy Kick</span><span>(20 SR)</span></div><div class="desc">(Carrot, Mango, Orange)</div></div>
      <div><div class="item"><span>Purple Thunder</span><span>(20 SR)</span></div><div class="desc">(Blackberry, Raspberry, Banana)</div></div>
      <div><div class="item"><span>Cool Breeze</span><span>(20 SR)</span></div><div class="desc">(Lemonade, Mint)</div></div>
      <div><div class="item"><span>Ruby Lantern</span><span>(20 SR)</span></div><div class="desc">(Lemonade, Strawberry, Mint)</div></div>
    </div>
  </section>

  <section class="panel greens">
    <h2>Mean Green Juices</h2>
    <div class="list">
      <div><div class="item"><span>Quick Sprout</span><span>(20 SR)</span></div><div class="desc">(Cucumber, Celery, Green Apple,<br>Spinach, Lemon, Ginger)</div></div>
      <div><div class="item"><span>Hop To It Now!</span><span>(20 SR)</span></div><div class="desc">(Carrots, Apple, Beetroot)</div></div>
    </div>
  </section>

  <section class="panel shakes">
    <div class="inner">
      <h2>Big Lift Zest</h2>
      <div class="group"><div class="desc" style="display:flex;justify-content:space-between;align-items:flex-end"><span>(Peanut Butter, Honey,<br>Skimmed Milk, Banana)</span><span style="font-size:12px;letter-spacing:1.3px">(20 SR)</span></div></div>
      <h2 style="margin-top:20px">Shake It Up</h2>
      <div class="group"><div class="item"><span>Dusky Swirl</span><span>(20 SR)</span></div><div class="desc">(Mocha, Skimmed Milk)</div></div>
      <div class="group"><div class="item"><span>Velvet Tumbler</span><span></span></div><div class="desc">(Chocolate, Skimmed Milk)</div></div>
    </div>
  </section>

  <div class="wordmark wordmark-left">Vartomel</div>

  <div class="tile" style="left:1124px;top:105px;width:70px;height:70px;background:#3f9a45" role="img" aria-label="Leaf sprig icon"></div>
  <div class="tile" style="left:1022px;top:179px;width:177px;height:95px;background:linear-gradient(90deg,#f29a2c,#e0441e)" role="img" aria-label="Dumbbell icon"></div>
  <div class="tile" style="left:600px;top:293px;width:120px;height:113px;background:#7fae3e" role="img" aria-label="Plate and cutlery icon"></div>
  <div class="tile" style="left:619px;top:409px;width:133px;height:83px;background:#4f9a3a" role="img" aria-label="Hand weight icon"></div>
  <div class="tile" style="left:978px;top:538px;width:124px;height:123px;background:#e1471f" role="img" aria-label="Steaming coffee cup icon"></div>
  <div class="tile" style="left:1108px;top:558px;width:85px;height:70px;background:#a9b23c" role="img" aria-label="Mug icon"></div>
  <div class="tile" style="left:956px;top:703px;width:118px;height:100px;background:#3f9142" role="img" aria-label="Tea cup icon"></div>
  <div class="tile" style="left:1081px;top:666px;width:115px;height:103px;background:#d9321c" role="img" aria-label="Soup bowl icon"></div>

  <div class="wordmark wordmark-top">Vartomel</div>

  <section class="panel bites">
    <h2>Yummy Bites</h2>
    <div class="list">
      <div class="item"><span>Zataar Croissant</span><span>(10 SR)</span></div>
      <div class="item"><span>Cheese Croissant</span><span>(10 SR)</span></div>
      <div class="item"><span>Plane Croissant</span><span>(10 SR)</span></div>
      <div class="item"><span>Blueberry Muffin</span><span>(07 SR)</span></div>
      <div class="item"><span>Chocolate Muffin</span><span>(07 SR)</span></div>
      <div class="item"><span>Vanilla Muffin</span><span>(07 SR)</span></div>
      <div class="item"><span>Cookies</span><span>(07 SR)</span></div>
      <div class="item"><span>Brownie</span><span>(10 SR)</span></div>
      <div class="item"><span>Resh Berry Popsicle</span><span>(10 SR)</span></div>
      <div class="item"><span>Fresh Orange Popsicle</span><span>(10 SR)</span></div>
    </div>
  </section>

  <section class="panel lite">
    <h2>Make It Lite</h2>
    <div class="list">
      <div class="item"><span>Garden Salad</span><span>(15 SR)</span></div>
      <div class="item"><span>Greek Salad</span><span>(15 SR)</span></div>
      <div class="item"><span>Ceaser Salad</span><span>(15 SR)</span></div>
      <div class="item"><span>Italian Salad</span><span>(15 SR)</span></div>
      <div class="item"><span>Tuna Sandwich</span><span>(25 SR)</span></div>
      <div class="item"><span>Turkey Sandwich</span><span>(25 SR)</span></div>
      <div class="item"><span>Chicken Sandwich</span><span>(25 SR)</span></div>
      <div class="item"><span>Happy Patch Bowls</span><span>(8SR)</span></div>
      <div class="item"><span>Mixed Nuts</span><span>(10 SR)</span></div>
    </div>
  </section>

  <section class="panel coffee">
    <h2>Coffee and Tea</h2>
    <div class="list">
      <div class="item"><span>Americano</span><span>(10 SR)</span></div>
      <div class="item"><span>Espresso</span><span>(10 SR)</span></div>
      <div class="item"><span>Turkish Coffee</span><span>(10 SR)</span></div>
      <div class="item"><span>Cappuccino</span><span>(15 SR)</span></div>
      <div class="item"><span>Cafe Latte</span><span>(15 SR)</span></div>
      <div class="item"><span>Hot Cacao</span><span>(15 SR)</span></div>
      <div class="item"><span>Extra Shor +</span><span>5SR&nbsp;&nbsp;</span></div>
      <div class="spacer"></div>
      <div class="item"><span>Green Tea</span><span>(10 SR)</span></div>
      <div class="item"><span>Earl Grey</span><span>(10 SR)</span></div>
      <div class="item"><span>English Breakfast</span><span>(10SR)</span></div>
    </div>
  </section>

  <div class="wordmark wordmark-bottom">Vartomel</div>
</main>
</body>
</html>
```